All Natural Mosquito Repellent

My company, BrightFern Company has created an all natural mosquito repellent. I already have other all natural products that I have developed and created labels for. I will include a copy of that label so you have something to work from. I will need two labels. One for the front of the bottle and one for the back. The back label will need space for a UPC. The labels need to be 63mm (H) x 39mm (W)

Target Market(s)

Consumers, Organic, People who like natural products

Font styles to use
Other font styles liked:
• A combination of both Serif and Sans Serif

Requirements
Must have
• Use the words Organic, All Natural, Travel size, made in the USA label
Nice to have
• tag line: Don't beat them off. Spray them away.

```html
<!DOCTYPE html>
<html lang="en">
<head>
<meta charset="utf-8">
<title>BrightFern Co. – All Natural Mosquito Repellent Labels</title>
<link href="https://fonts.googleapis.com/css2?family=Open+Sans:wght@400;600;700&family=Oswald:wght@500;700&family=Roboto+Condensed:ital,wght@1,400&display=swap" rel="stylesheet">
<style>
  :root {
    --bg-light: #f2f2f2;
    --bg-dark: #cfcfcf;
    --forest: #0e3d1f;
    --forest-deep: #0a3018;
    --sun-top: #f7b21a;
    --sun-low: #f28a12;
    --tree: #1f5a26;
    --accent-red: #d8401c;
    --brand-brown: #7a4a1c;
    --ink-light: #ffffff;
    --ink-muted: #e6ece7;
  }
  * { margin: 0; padding: 0; box-sizing: border-box; }
  html, body { width: 1200px; height: 1200px; overflow: hidden; }
  body {
    background: radial-gradient(circle at 50% 40%, var(--bg-light) 0%, var(--bg-dark) 100%);
    font-family: "Open Sans", Arial, sans-serif;
    position: relative;
  }
  .label {
    position: absolute;
    top: 262px;
    width: 420px;
    height: 678px;
    border-radius: 12px;
    overflow: hidden;
    background: var(--forest);
    color: var(--ink-light);
  }
  .label--front { left: 130px; }
  .label--back { left: 650px; }

  /* Front label */
  .sky {
    position: absolute; left: 0; top: 0; width: 100%; height: 250px;
    background: linear-gradient(180deg, var(--sun-top) 0%, var(--sun-low) 100%);
  }
  .brand {
    position: absolute; top: 24px; left: 0; width: 100%;
    display: flex; flex-direction: column; align-items: center;
  }
  .brand__mark {
    width: 110px; height: 110px; border-radius: 50%;
    background: var(--forest);
  }
  .brand__name {
    margin-top: 12px;
    font-family: "Open Sans", Arial, sans-serif;
    font-weight: 600; font-size: 26px; letter-spacing: 1px;
    color: var(--brand-brown);
  }
  .brand__note {
    margin-top: 2px; font-size: 10px; color: var(--brand-brown);
    width: 240px; display: flex; justify-content: space-between;
  }
  .treeline {
    position: absolute; left: 0; top: 180px; width: 100%; height: 90px;
    background: linear-gradient(180deg, rgba(31,90,38,0) 0%, var(--tree) 45%, var(--forest) 100%);
  }
  .product-name {
    position: absolute; top: 278px; width: 100%; text-align: center;
    font-family: "Oswald", Arial, sans-serif; font-weight: 700;
    font-size: 30px; line-height: 32px; font-style: italic;
    color: var(--accent-red);
    -webkit-text-stroke: 1px var(--ink-light);
    text-transform: uppercase;
  }
  .product-attrs {
    position: absolute; top: 350px; width: 100%; text-align: center;
    font-size: 14px; color: var(--ink-muted); letter-spacing: 0.5px;
  }
  .tagline {
    position: absolute; top: 395px; left: 0; width: 100%; height: 110px;
  }
  .tagline__text {
    position: absolute; top: 30px; width: 100%; text-align: center;
    font-family: "Roboto Condensed", Arial, sans-serif; font-style: italic;
    font-size: 27px; line-height: 32px;
  }
  .tagline svg { position: absolute; left: 0; top: 0; }
  .shield { position: absolute; left: 182px; top: 522px; }
  .volume {
    position: absolute; left: 335px; top: 555px;
    font-size: 13px; font-weight: 600;
  }
  .protection {
    position: absolute; left: 40px; top: 570px;
    transform: rotate(-16deg);
    font-family: "Oswald", Arial, sans-serif; font-weight: 700;
    font-size: 16px; line-height: 16px; text-align: center;
    color: var(--accent-red); -webkit-text-stroke: 0.6px var(--ink-light);
  }
  .hill { position: absolute; left: 0; top: 575px; }
  .origin {
    position: absolute; top: 625px; width: 100%; text-align: center;
    font-size: 19px; color: var(--ink-muted);
  }

  /* Back label */
  .info { position: absolute; top: 38px; left: 30px; right: 30px; text-align: center; }
  .info__section { margin-bottom: 20px; }
  .info__heading {
    display: inline-block; border: 1.5px solid var(--ink-light); border-radius: 3px;
    padding: 2px 10px; font-size: 13px; font-weight: 700; text-transform: uppercase;
    margin-bottom: 10px;
  }
  .info__text { font-size: 9.5px; line-height: 13px; color: var(--ink-muted); }
  .address { position: absolute; top: 432px; left: 112px; width: 220px; }
  .address__title { font-size: 16px; font-weight: 700; text-align: center; margin-bottom: 6px; }
  .address__text { font-size: 13.5px; line-height: 18px; }
  .recycle { position: absolute; left: 22px; top: 552px; }
  .upc {
    position: absolute; left: 108px; top: 532px; width: 280px; height: 82px;
    border: 2px solid var(--ink-light);
    display: flex; align-items: center; justify-content: center;
    font-size: 28px; font-weight: 600;
  }
</style>
</head>
<body>

<section class="label label--front" aria-label="Front label">
  <div class="sky"></div>
  <div class="brand">
    <div class="brand__mark"></div>
    <div class="brand__name">BRIGHTFERN CO.</div>
    <div class="brand__note"><span>crafted by hand, with love</span><span>in the U.S.A.</span></div>
  </div>
  <div class="treeline" role="img" aria-label="Silhouette of a pine forest skyline"></div>

  <h1 class="product-name">All Natural<br>Mosquito Repellent</h1>
  <p class="product-attrs">ORGANIC &#9679; TRAVEL SIZE</p>

  <div class="tagline">
    <svg width="420" height="110" viewBox="0 0 420 110" aria-hidden="true">
      <path d="M148 22 Q210 2 272 14 Q210 10 148 22 Z" fill="#ffffff"/>
      <path d="M148 94 Q210 110 272 92 Q210 102 148 94 Z" fill="#ffffff"/>
    </svg>
    <p class="tagline__text">“Don’t beat them off<br>Spray them away”</p>
  </div>

  <svg class="shield" width="56" height="64" viewBox="0 0 56 64" aria-hidden="true">
    <path d="M28 2 L53 10 Q53 44 28 62 Q3 44 3 10 Z" fill="#ffffff" stroke="#b9c4bc" stroke-width="2"/>
  </svg>
  <div class="volume">50 ML</div>
  <div class="protection">12 HOUR<br>PROTECTION</div>

  <svg class="hill" width="420" height="40" viewBox="0 0 420 40" aria-hidden="true">
    <path d="M0 38 Q210 -4 420 30" fill="none" stroke="#d9e2db" stroke-width="2"/>
  </svg>
  <p class="origin">Made in the USA</p>
</section>

<section class="label label--back" aria-label="Back label">
  <div class="info">
    <div class="info__section">
      <h2 class="info__heading">Direction for use:</h2>
      <p class="info__text">There are many variations of passages of Lorem Ipsum available, but the majority have suffered alteration in some form, by injected humour, or randomised words which don't look even slightly believable. If you are going to use a passage of Lorem Ipsum, you need to be sure there isn't anything embarrassing hidden in the middle of text.</p>
    </div>
    <div class="info__section">
      <h2 class="info__heading">Precaution:</h2>
      <p class="info__text">There are many variations of passages of Lorem Ipsum available, but the majority have suffered alteration in some form, by injected humour, or randomised words which don't look even slightly believable.</p>
    </div>
    <div class="info__section">
      <h2 class="info__heading">Ingredients:</h2>
      <p class="info__text">There are many variations of passages of Lorem Ipsum available, but the majority have suffered alteration in some form, by injected humour, or randomised words which don't look even slightly believable.</p>
    </div>
    <div class="info__section">
      <h2 class="info__heading">Storage:</h2>
      <p class="info__text">Store in a cool and dry place. Place empty container in<br>trash or recycle.</p>
    </div>
  </div>

  <div class="address">
    <h3 class="address__title">Company Address:</h3>
    <p class="address__text">Lorem Ipsum is simply dummy text of the printing and typesetting industry.</p>
  </div>

  <svg class="recycle" width="44" height="40" viewBox="0 0 44 40" aria-label="Recyclable" role="img">
    <g fill="none" stroke="#ffffff" stroke-width="4" stroke-linejoin="round">
      <path d="M14 14 L22 3 L29 13"/>
      <path d="M34 20 L40 32 L27 33"/>
      <path d="M17 34 L4 33 L10 21"/>
    </g>
    <g fill="#ffffff">
      <path d="M25 9 L33 10 L29 17 Z"/>
      <path d="M30 31 L25 37 L23 29 Z"/>
      <path d="M8 25 L4 18 L12 18 Z"/>
    </g>
  </svg>
  <div class="upc">UPC</div>
</section>

</body>
</html>
```